Brindle Pet Shop Homepage

We are a pet shop, we focus on dog food / cat food / rodents & bird food

Based on WooCommerce

It should be a simple but professional homepage with an informative start page. In the shop it should then be possible to shop for products/manufacturers etc. Navigation/Filter menu on the left would be ideal.

Next menus:
ABOUT US
CONTACT
DOG
CAT
HOLDER

My Account - Login
My Cart

Footer:
Conditions
payment options
social media

In addition to our logo, I have attached 2 example pages from another shop which we would use as a guideline.

Target Market(s)

pet store

Industry/Entity Type

Animal, Pet Shop

Coding

Coded - Design and coding required

Number of Pages Required

1 page

Font styles to use
Sans Serif

Colors
0054AA
0677BA
7BADD7
CADEEF
E8F1F8

Requirements
Must have
• Main Page, Contact, About Us, Shop, Check Out, Member Login, Mailchimp Marketing - We work with WooCommerce

```html
<!DOCTYPE html>
<html lang="en">
<head>
<meta charset="utf-8">
<title>Brindle Pet Shop</title>
<link href="https://fonts.googleapis.com/css2?family=Arimo:wght@400;500;700&display=swap" rel="stylesheet">
<style>
:root{
  --blue-deep:#0054AA;
  --blue:#0677BA;
  --blue-mid:#7BADD7;
  --blue-soft:#CADEEF;
  --blue-pale:#E8F1F8;
  --ink:#111111;
  --text:#3a3a3a;
  --muted:#6b6b6b;
  --white:#ffffff;
  --bar:#F3F5FC;
}
*{margin:0;padding:0;box-sizing:border-box}
html,body{width:1200px;height:3058px;overflow:hidden}
body{font-family:"Arimo",Helvetica,Arial,sans-serif;color:var(--text);background:var(--white);position:relative}
.abs{position:absolute}
.btn{display:inline-flex;align-items:center;justify-content:center;height:41px;padding:0 22px;border-radius:4px;background:var(--blue-deep);color:var(--white);font-size:14px;letter-spacing:1.4px;text-transform:uppercase;text-decoration:none;font-weight:500}
.btn-outline{background:var(--white);color:var(--blue-deep);border:2px solid var(--blue-deep)}
.photo{position:absolute}

/* header */
.site-header{top:0;left:0;width:1200px;height:68px;background:var(--white)}
.brand{left:107px;top:21px;display:flex;align-items:center;gap:8px;font-size:17px;font-weight:700;color:var(--blue-deep)}
.brand-dot{width:22px;height:22px;border-radius:50%;background:var(--blue-deep)}
.main-nav{left:409px;top:26px;display:flex;gap:34px;font-size:14px;color:var(--ink)}
.user-nav{right:107px;top:24px;display:flex;gap:22px;font-size:14px;color:var(--ink);align-items:center}
.user-nav span{display:flex;align-items:center;gap:7px}

/* hero */
.hero{top:68px;left:0;width:1200px;height:562px;background:var(--blue-pale);overflow:hidden}
.hero h1{left:107px;top:124px;font-size:45px;line-height:60px;font-weight:700;color:var(--ink);width:560px}
.hero .lede{left:107px;top:326px;width:520px;font-size:13.5px;line-height:27px}
.hero .actions{left:107px;top:401px;display:flex;gap:18px}
.hero .actions .btn{height:42px}

/* welcome */
.welcome h2{left:523px;top:792px;font-size:30px;font-weight:700;color:var(--ink)}
.welcome .body{left:523px;top:855px;width:565px;font-size:13.5px;line-height:27px}

/* products */
.products h2{left:0;top:1274px;width:1200px;text-align:center;font-size:30px;font-weight:700;color:var(--ink)}
.products .intro{left:280px;top:1330px;width:640px;text-align:center;font-size:13.5px;line-height:27px}
.card{top:1415px;width:321px;height:290px;background:var(--white);border-radius:6px;box-shadow:0 2px 14px rgba(0,0,0,.07);text-align:center}
.card .icon{width:112px;height:112px;border-radius:50%;background:var(--blue-pale);margin:31px auto 0;display:flex;align-items:center;justify-content:center}
.card .icon-fill{width:62px;height:62px;border-radius:50%;background:var(--blue-soft)}
.card h3{margin-top:30px;font-size:19px;font-weight:700;color:var(--ink)}
.card .btn{margin-top:25px;height:40px;padding:0 20px}

/* newsletter */
.ask{left:107px;top:1842px;width:987px;height:281px;border-radius:30px;background:linear-gradient(100deg,var(--blue) 0%,#3c8ccb 60%,#64a6da 100%);overflow:hidden}
.ask h2{left:0;top:58px;width:987px;text-align:center;font-size:30px;font-weight:700;color:var(--white)}
.ask p{left:313px;top:120px;width:360px;text-align:center;font-size:11px;line-height:20px;color:var(--white)}
.subscribe{left:292px;top:181px;width:402px;height:45px;background:var(--white);border-radius:6px;display:flex;align-items:center;justify-content:space-between;padding:0 3px 0 24px;border:2px solid var(--white)}
.subscribe span{font-size:11.5px;color:var(--muted)}
.subscribe b{height:37px;padding:0 22px;background:var(--blue-deep);color:var(--white);font-size:10.5px;border-radius:5px;display:flex;align-items:center}

/* nutrition */
.nutrition h2{left:619px;top:2236px;font-size:38px;line-height:44px;font-weight:700;color:var(--ink)}
.nutrition .lede{left:619px;top:2345px;width:460px;font-size:13.5px;line-height:27px}
.checks{left:619px;top:2418px;list-style:none;font-size:13.5px;color:var(--ink)}
.checks li{display:flex;align-items:center;gap:8px;height:34.5px}

/* footer */
.site-footer{top:2720px;left:0;width:1200px;height:280px;background:var(--blue-pale)}
.foot-col{top:45px}
.foot-col h4{font-size:18px;font-weight:700;color:var(--ink);margin-bottom:14px}
.foot-col li{list-style:none;font-size:13px;color:var(--muted);line-height:25.6px}
.contact-line{display:flex;align-items:center;gap:11px;color:var(--blue-deep);font-size:13.5px;margin-top:12px}
.copyright{top:3000px;left:0;width:1200px;height:58px;background:var(--bar);font-size:13px;color:var(--muted);padding:26px 0 0 116px}
</style>
</head>
<body>

<header class="site-header abs">
  <div class="brand abs"><span class="brand-dot"></span>Brindle Pet</div>
  <nav class="main-nav abs"><span>ABOUT US</span><span>CONTACT</span><span>DOG</span><span>CAT</span><span>HOLDER</span></nav>
  <div class="user-nav abs">
    <span><svg width="16" height="16" viewBox="0 0 16 16" fill="none" stroke="#111" stroke-width="1.3"><circle cx="8" cy="5" r="3.2"/><path d="M2 15c0-3.3 2.7-5 6-5s6 1.7 6 5z"/></svg>LOG IN</span>
    <span><svg width="18" height="16" viewBox="0 0 18 16" fill="none" stroke="#111" stroke-width="1.3"><path d="M1 1.5h2.5l2 9h9l2-6.5H4.4"/><circle cx="7" cy="14" r="1.2"/><circle cx="14" cy="14" r="1.2"/></svg>CART</span>
  </div>
</header>

<section class="hero abs">
  <h1 class="abs">Feed Your Furry Friends The Best With Our Premium Pet Food!</h1>
  <p class="lede abs">Our carefully curated selection of high-quality products will keep your pets healthy, happy, and satisfied. Shop now and give your pets the nutrition they deserve</p>
  <div class="actions abs"><a class="btn">Shop Now</a><a class="btn btn-outline">View Our Products</a></div>
  <svg class="abs" style="left:690px;top:60px" width="520" height="330" viewBox="0 0 520 330"><ellipse cx="265" cy="155" rx="250" ry="125" fill="none" stroke="var(--blue-soft)" stroke-width="7" transform="rotate(-10 265 155)"/></svg>
  <div class="photo" role="img" aria-label="Tri-colour dog wearing sunglasses" style="left:700px;top:122px;width:500px;height:440px;border-radius:210px 210px 0 0;background:linear-gradient(180deg,#3a2a22,#1b1613 60%,#2a211c)"></div>
</section>

<section class="welcome">
  <svg class="abs" style="left:115px;top:805px" width="320" height="360" viewBox="0 0 320 360"><ellipse cx="160" cy="175" rx="140" ry="170" fill="var(--blue-pale)"/><ellipse cx="160" cy="175" rx="145" ry="172" fill="none" stroke="var(--blue-mid)" stroke-width="6" transform="rotate(12 160 175)"/></svg>
  <div class="photo" role="img" aria-label="Ginger kitten sitting" style="left:170px;top:755px;width:200px;height:385px;border-radius:90px 90px 40px 40px;background:linear-gradient(180deg,#e2b48a,#d39a68)"></div>
  <h2 class="abs">Welcome To Brindle Pet</h2>
  <p class="body abs">Lorem ipsum dolor sit amet consectetur. Malesuada justo lectus sit vestibulum. Maecenas sed laoreet sapien risus arcu pharetra. Nunc vestibulum ut quisque venenatis. A facilisis morbi cursus vestibulum phasellus purus aenean phasellus amet. Praesent proin faucibus habitant vulputate donec urna sed. Mattis id augue molestie viverra in amet. Turpis suscipit pharetra feugiat non fermentum.<br>Elementum non sagittis leo porta massa dolor amet sed. Augue magnis suscipit in molestie. Ullamcorper bibendum egestas egestas et eleifend bibendum ut. Sem egestas.</p>
  <a class="btn abs" style="left:523px;top:1071px">Know More</a>
</section>

<section class="products">
  <h2 class="abs">Products For Your Furry Friends</h2>
  <p class="intro abs">Lorem ipsum dolor sit amet consectetur. Malesuada justo lectus sit vestibulum. Maecenas sed laoreet sapien risus arcu pharetra. Nunc vestibulum ut quisque venenatis</p>
  <article class="card abs" style="left:107px">
    <div class="icon"><div class="icon-fill" role="img" aria-label="Line icon of a dog's head"></div></div>
    <h3>Everything For Your Dog</h3><a class="btn">View Products</a>
  </article>
  <article class="card abs" style="left:440px">
    <div class="icon"><div class="icon-fill" role="img" aria-label="Line icon of a cat's head"></div></div>
    <h3>Everything For Your Cat</h3><a class="btn">View Products</a>
  </article>
  <article class="card abs" style="left:773px">
    <div class="icon"><svg width="70" height="70" viewBox="0 0 70 70" fill="none" stroke="var(--blue-deep)" stroke-width="3.2" stroke-linecap="round"><circle cx="22" cy="22" r="14"/><path d="M22 36v22M13 48h18"/><circle cx="47" cy="50" r="13"/><path d="M47 37V12M40 19l7-7 7 7"/></svg></div>
    <h3>Mistress &amp; Mister</h3><a class="btn">View Products</a>
  </article>
</section>

<section class="ask abs">
  <svg class="abs" style="left:20px;top:80px" width="200" height="220" viewBox="0 0 200 220"><ellipse cx="95" cy="110" rx="80" ry="100" fill="none" stroke="var(--blue-mid)" stroke-width="4" transform="rotate(25 95 110)"/></svg>
  <div class="photo" role="img" aria-label="Tabby cat" style="left:40px;top:130px;width:115px;height:151px;border-radius:60px 60px 0 0;background:linear-gradient(180deg,#8a7560,#5e4e3f)"></div>
  <svg class="abs" style="left:655px;top:90px" width="300" height="200" viewBox="0 0 300 200"><ellipse cx="150" cy="100" rx="140" ry="75" fill="none" stroke="var(--blue-mid)" stroke-width="4" transform="rotate(-12 150 100)"/></svg>
  <div class="photo" role="img" aria-label="Golden retriever" style="left:765px;top:88px;width:140px;height:193px;border-radius:65px 65px 0 0;background:linear-gradient(180deg,#c98a4a,#a96a32)"></div>
  <h2 class="abs">Feel free to ask us anything</h2>
  <p class="abs">Brindle Grooming provides grooming services for all dog and cat breeds. We are fully committed to the health.</p>
  <div class="subscribe abs"><span>Your email address</span><b>Subscribe Now</b></div>
</section>

<section class="nutrition">
  <svg class="abs" style="left:160px;top:2300px" width="310" height="340" viewBox="0 0 310 340"><ellipse cx="155" cy="170" rx="135" ry="160" fill="var(--blue-pale)"/><ellipse cx="155" cy="170" rx="135" ry="160" fill="none" stroke="var(--blue-mid)" stroke-width="6" transform="rotate(14 155 170)"/></svg>
  <div class="photo" role="img" aria-label="Red and white dog sitting" style="left:215px;top:2255px;width:200px;height:360px;border-radius:90px 90px 40px 40px;background:linear-gradient(180deg,#c7773a,#b0642c 70%,#d9b89a)"></div>
  <h2 class="abs">Totally nutritious<br>ven-baked delicious</h2>
  <p class="lede abs">Brindle Grooming provides grooming services for all dog and cat breeds. We are fully committed to the health.</p>
  <ul class="checks abs">
    <li><svg width="11" height="9" viewBox="0 0 11 9"><path d="M1 4.5l3 3L10 1" fill="none" stroke="var(--blue-deep)" stroke-width="2"/></svg>Talk to highly qualified vet online on chat/call</li>
    <li><svg width="11" height="9" viewBox="0 0 11 9"><path d="M1 4.5l3 3L10 1" fill="none" stroke="var(--blue-deep)" stroke-width="2"/></svg>Save time &amp; money</li>
    <li><svg width="11" height="9" viewBox="0 0 11 9"><path d="M1 4.5l3 3L10 1" fill="none" stroke="var(--blue-deep)" stroke-width="2"/></svg>No hassle of prior appointments</li>
    <li><svg width="11" height="9" viewBox="0 0 11 9"><path d="M1 4.5l3 3L10 1" fill="none" stroke="var(--blue-deep)" stroke-width="2"/></svg>2nd opnion from experts</li>
  </ul>
  <a class="btn abs" style="left:619px;top:2567px">Shop Now</a>
</section>

<footer class="site-footer abs">
  <div class="foot-col abs" style="left:116px">
    <h4>Store location</h4>
    <ul><li style="line-height:18px;width:200px">412 Willowbrook Lane Fairhaven, OR 97410</li></ul>
    <div class="contact-line" style="margin-top:16px"><svg width="20" height="20" viewBox="0 0 20 20"><rect x="4" y="6" width="12" height="9" rx="1" fill="none" stroke="var(--blue-mid)" stroke-width="1.3"/><path d="M4 7l6 4 6-4" fill="none" stroke="var(--blue-mid)" stroke-width="1.3"/></svg>hello@brindlepet.shop</div>
    <div class="contact-line"><svg width="20" height="20" viewBox="0 0 20 20"><path d="M6 4l2.5 3-1.5 1.5c.8 1.8 2 3 3.8 3.8L12.3 11l3 2.5-1.5 2C9 15 5 11 4.5 5.5z" fill="none" stroke="var(--blue-mid)" stroke-width="1.3"/></svg>(1800)-55-42-317</div>
  </div>
  <div class="foot-col abs" style="left:476px"><h4>Information</h4><ul><li>About us</li><li>Blog</li><li>Check out</li><li>Contact</li><li>Service</li></ul></div>
  <div class="foot-col abs" style="left:678px"><h4>My account</h4><ul><li>My Account</li><li>Contact</li><li>Shopping cart</li><li>Shop</li></ul></div>
  <div class="foot-col abs" style="left:881px"><h4>Categories</h4><ul><li>Fruits &amp; Vegetables</li><li>Dairy Products</li><li>Package Foods</li><li>Beverage</li><li>Health &amp; Wellness</li></ul></div>
</footer>
<div class="copyright abs">Copyright © 2023 All rights recived</div>

</body>
</html>
```